National appliance rental company needs a newspaper ad design

We need an ad template that we can use for different newspaper advertising. Ad is to be colourful - I have attached our current marketing so you have an idea of colours.
Text to be something like the below:

Want it, Rent it, Own it!

Need to update your furniture? Kids need stuff for school?

(Put in pics of phones and TV)

Tablix starting from just $8 per week
Smart phones starting from $10 per week
Large family fridges from $30 per week

TV’s, laptops, whitegoods, furniture, beds – we will finance just about anything!

Fast approvals – call 1300 582 961 or go to www.brightgoodshire.example.au/apply - NOW!
$50 credit voucher given to the first 10 successful applicants.

(Pic of logo somewhere)
Terms and conditions apply. Pricing based on 24 month term

Harbourline Goods Hire P/L ACN 061 247 893. Australian Credit Licence # 718294

Target Market(s)

Low income people and families

Industry/Entity Type

Appliance

Requirements
Must have
• I would love to have a couple of different sizes.
• Maybe 6cm x 10 cm, and also 10cms x 10cms.
Nice to have
• Please use the green from fridge magnet and colours from our logo, etc.

```html
<!DOCTYPE html>
<html lang="en">
<head>
<meta charset="utf-8">
<title>Harbourline Goods Hire – Newspaper Ad</title>
<link rel="stylesheet" href="https://fonts.googleapis.com/css2?family=Bebas+Neue&family=Oswald:wght@500;600;700&family=Roboto+Condensed:wght@400;700&family=Lato:ital,wght@0,400;0,700;0,900;1,400&display=swap">
<style>
  :root {
    --page-bg: #e9e6e1;
    --ad-green: #7cc242;
    --ad-green-light: #92d255;
    --ad-green-dark: #5ea52c;
    --ad-red: #e31e24;
    --ad-red-dark: #b8141a;
    --ad-lime: #d8f23c;
    --ad-navy: #26358f;
    --ad-navy-dark: #17216a;
    --ad-sky: #1a8fd6;
    --ad-white: #ffffff;
    --ad-ink: #2b2b2b;
  }
  * { box-sizing: border-box; margin: 0; padding: 0; }
  html, body { width: 904px; height: 1200px; overflow: hidden; }
  body { background: var(--page-bg); position: relative; font-family: "Lato", sans-serif; }

  .ad {
    position: absolute; left: 109px; top: 30px;
    width: 686px; height: 1140px; overflow: hidden;
    background: radial-gradient(ellipse at 50% 40%, var(--ad-green-light), var(--ad-green) 60%, var(--ad-green-dark));
  }
  .ad > * { position: absolute; }

  .mascot-art { left: 109px; top: 8px; width: 121px; height: 208px; border-radius: 14px;
    background: linear-gradient(160deg, #ffffff, #d4d8d9); }

  .brand-name { left: 250px; top: 58px; width: 330px;
    font-family: "Oswald", sans-serif; font-weight: 700; font-size: 50px; line-height: 1;
    color: var(--ad-red); text-transform: uppercase; }
  .brand-tagline { left: 300px; top: 184px; font-family: "Lato", sans-serif; font-style: italic;
    font-weight: 700; font-size: 19px; color: var(--ad-ink); }

  .headline { left: 0; top: 222px; width: 100%; text-align: center;
    font-family: "Bebas Neue", sans-serif; font-size: 84px; line-height: 1; color: var(--ad-white);
    text-shadow: 2px 3px 4px rgba(0,0,0,.45); letter-spacing: 1px; }

  .questions { left: 0; top: 312px; width: 100%; text-align: center;
    font-family: "Oswald", sans-serif; font-weight: 600; font-size: 27px; line-height: 1.15;
    color: var(--ad-red); text-transform: uppercase; }

  .phones-art { left: 53px; top: 420px; width: 242px; height: 124px; border-radius: 6px;
    background: linear-gradient(90deg, #dfe3e6, #2a2d33 45%, #5fa7e0 75%, #222); }
  .tv-art { left: 350px; top: 380px; width: 285px; height: 186px; border-radius: 4px;
    background: linear-gradient(180deg, #1d6fc4, #52b4ea 60%, #e8f4fb 80%, #1a1a1a 82%); }

  .price-panel { left: 0; top: 595px; width: 481px; height: 140px;
    background: linear-gradient(180deg, #ef3036, var(--ad-red-dark));
    border-radius: 0 22px 22px 0; border: 2px solid #ffffff;  border-left: none;
    padding: 16px 0 0 16px; }
  .price-line { font-family: "Lato", sans-serif; font-size: 21px; color: var(--ad-white); line-height: 40px; }
  .price-line strong { color: var(--ad-lime); font-weight: 900; }

  .heater-art { left: 503px; top: 615px; width: 71px; height: 98px; border-radius: 10px;
    background: linear-gradient(180deg, #d9dcde, #f39a3c 40%, #c8ccce); }
  .washer-art { left: 578px; top: 555px; width: 95px; height: 175px;
    background: linear-gradient(180deg, #f4f4f4, #d9dcdd); }

  .ribbon { left: 11px; top: 752px; width: 662px; height: 120px; }
  .ribbon-text { left: 11px; top: 766px; width: 662px; text-align: center;
    font-family: "Roboto Condensed", sans-serif; line-height: 1.2; }
  .ribbon-text .items { font-size: 31px; color: var(--ad-white); }
  .ribbon-text .offer { font-size: 30px; font-weight: 700; color: var(--ad-lime); text-transform: uppercase; letter-spacing: .5px; }

  .call-to-action { left: 16px; top: 886px; width: 470px;
    font-family: "Bebas Neue", sans-serif; font-size: 29px; line-height: 1.25; color: var(--ad-white); }
  .call-to-action .hot { color: var(--ad-red); }

  .voucher { left: 457px; top: 877px; width: 221px; height: 208px; }
  .voucher-text { left: 477px; top: 940px; width: 181px; text-align: center;
    font-family: "Lato", sans-serif; font-weight: 900; font-size: 21px; line-height: 1.08; color: var(--ad-white); }
  .voucher-text .lime { color: var(--ad-lime); }

  .licence-box { left: 11px; top: 1009px; width: 399px; height: 93px;
    background: var(--ad-sky); border-radius: 14px; padding: 8px 14px;
    font-family: "Lato", sans-serif; font-size: 19px; line-height: 1.3; color: var(--ad-white); }

  .terms { left: 0; top: 1106px; width: 100%; text-align: center;
    font-family: "Lato", sans-serif; font-style: italic; font-size: 17px; color: var(--ad-ink); }
</style>
</head>
<body>
  <main class="ad">
    <div class="mascot-art" role="img" aria-label="Cartoon fridge mascot character"></div>
    <div class="brand-name">Harbourline Goods Hire</div>
    <div class="brand-tagline">“It’s cheaper to hire local!”</div>

    <h1 class="headline">Want it, Rent it, Own it!</h1>
    <p class="questions">Need to update your furniture?<br>Kids need stuff for school?</p>

    <div class="phones-art" role="img" aria-label="Row of smartphones"></div>
    <div class="tv-art" role="img" aria-label="Flat screen TV showing a surfer on a wave"></div>

    <section class="price-panel">
      <p class="price-line">Tablix starting from just <strong>$8 PER WEEK</strong></p>
      <p class="price-line">Smart phones starting from <strong>$10 PER WEEK</strong></p>
      <p class="price-line">Large family fridges from <strong>$30 PER WEEK</strong></p>
    </section>

    <div class="heater-art" role="img" aria-label="Portable heater"></div>
    <div class="washer-art" role="img" aria-label="Washing machine with towel"></div>

    <svg class="ribbon" viewBox="0 0 662 120" preserveAspectRatio="none" aria-hidden="true">
      <polygon points="0,28 56,28 56,118 0,118 20,73" fill="var(--ad-navy)"/>
      <polygon points="662,28 606,28 606,118 662,118 642,73" fill="var(--ad-navy)"/>
      <polygon points="36,100 56,100 56,118" fill="var(--ad-navy-dark)"/>
      <polygon points="626,100 606,100 606,118" fill="var(--ad-navy-dark)"/>
      <rect x="36" y="6" width="590" height="94" fill="var(--ad-navy)"/>
      <rect x="42" y="11" width="578" height="84" fill="none" stroke="#ffffff" stroke-width="1.5" stroke-dasharray="6 4"/>
    </svg>
    <div class="ribbon-text">
      <div class="items">TV’s, laptops, whitegoods, furniture, beds</div>
      <div class="offer">We will finance just about anything!</div>
    </div>

    <p class="call-to-action">Fast approvals call <span class="hot">1300 582 961</span> or<br>go to <span class="hot">www.brightgoodshire.example.au/</span><br>apply - now!</p>

    <svg class="voucher" viewBox="0 0 200 200" preserveAspectRatio="none" aria-hidden="true">
      <polygon fill="var(--ad-red)" stroke="#ffffff" stroke-width="2" points="200,100 184.4,116.8 192.4,138.3 171.5,147.8 170.7,170.7 147.8,171.5 138.3,192.4 116.8,184.4 100,200 83.2,184.4 61.7,192.4 52.2,171.5 29.3,170.7 28.5,147.8 7.6,138.3 15.6,116.8 0,100 15.6,83.2 7.6,61.7 28.5,52.2 29.3,29.3 52.2,28.5 61.7,7.6 83.2,15.6 100,0 116.8,15.6 138.3,7.6 147.8,28.5 170.7,29.3 171.5,52.2 192.4,61.7 184.4,83.2"/>
    </svg>
    <p class="voucher-text">$50 credit voucher given to the first <span class="lime">10 successful applicants</span></p>

    <div class="licence-box">Harbourline Goods Hire P/L ACN 061 247 893. Australian Credit Licence # 718294</div>

    <p class="terms">Terms and conditions apply. Pricing based on 24 month term</p>
  </main>
</body>
</html>
```